7 page website for Dog Training Business

we are seeking a website design that should be 7 pages for a Las Vegas Dog training business. the site will have a heavy focus on video, and social media. Ideas design can be borrowed from http://plumcrestway.net
attached is a copy of the logo and business card mock up. Content is currently being written and will be posted shortly

Training

```html
<!DOCTYPE html>
<html lang="en">
<head>
<meta charset="utf-8">
<title>Plumcrest – Dog Training</title>
<link rel="stylesheet" href="https://fonts.googleapis.com/css2?family=Lato:wght@300;400;700&family=Great+Vibes&display=swap">
<style>
:root{
  --leaf:#b7d65c;
  --leaf-dark:#4f6b12;
  --leaf-pale:#eef5d8;
  --bark:#7b4124;
  --bark-dark:#5a2e18;
  --amber:#f2a52b;
  --ink:#333;
  --muted:#666;
  --paper:#fff;
}
*{box-sizing:border-box;margin:0;padding:0}
html,body{width:890px;height:1200px;overflow:hidden}
body{position:relative;font-family:'Lato',sans-serif;color:var(--ink);background:var(--paper)}
.backdrop{position:absolute;inset:0;background:radial-gradient(circle at 50% 50%,#fbfdf4 0%,var(--leaf-pale) 60%,#dcebb0 100%)}
.page{position:absolute;left:72px;top:34px;width:745px;height:1132px;background:var(--paper);box-shadow:0 0 4px rgba(0,0,0,.35)}
.nav-band{position:absolute;left:40px;top:75px;width:814px;height:47px;background:var(--leaf);border-radius:8px}
.nav-tab-left{position:absolute;left:48px;top:59px;width:30px;height:16px;background:var(--leaf-dark);border-radius:8px 0 0 0}
.nav-tab-right{position:absolute;left:817px;top:122px;width:30px;height:16px;background:var(--leaf-dark);border-radius:0 0 8px 0}
.brand{position:absolute;left:91px;top:48px;width:104px;height:104px;border-radius:50%;background:var(--paper);border:4px solid var(--leaf);box-shadow:0 2px 4px rgba(0,0,0,.3);display:flex;align-items:center;justify-content:center}
.brand-name{font-weight:700;font-size:15px;color:var(--bark);letter-spacing:.5px}
.social-top{position:absolute;left:400px;top:47px;display:flex;gap:12px}
.social-top span{width:10px;height:10px;border-radius:50%;background:var(--bark)}
.search{position:absolute;left:635px;top:47px;width:163px;height:16px;border-bottom:1px solid #999;font-size:9px;color:#777;padding-top:2px}
.search svg{position:absolute;right:2px;top:2px}
.main-nav{position:absolute;left:247px;top:92px;display:flex;gap:20px;font-size:11px;color:#3a2a10}
.main-nav .current{color:var(--bark)}
.hero{position:absolute;left:92px;top:163px;width:706px;height:292px;background:linear-gradient(100deg,#8a8a2a 0%,#c99a45 45%,#e3b36a 65%,#7a6a3a 100%)}
.hero-shadow{position:absolute;left:130px;top:455px;width:630px;height:40px;background:radial-gradient(ellipse at 50% 0,rgba(0,0,0,.18),transparent 70%)}
.hero-copy{position:absolute;left:237px;top:200px;color:#fff}
.hero-title{font-size:31px;font-weight:400;line-height:33px}
.hero-sub{font-size:12px;line-height:16px;margin-top:7px;font-weight:300}
.hero-btn{display:inline-flex;align-items:center;gap:8px;margin-top:8px;background:var(--amber);color:#fff;font-size:12px;padding:3px 9px}
.dots{position:absolute;display:flex;gap:4px}
.dots span{width:6px;height:6px;border-radius:50%;background:#bbb}
.dots .on{background:var(--bark)}
.welcome{position:absolute;left:92px;top:492px;font-family:'Great Vibes',cursive;font-size:34px;color:var(--bark)}
.intro{position:absolute;left:92px;top:551px;width:222px;text-align:justify}
.intro h2{font-size:12px;font-weight:400;line-height:14px}
.intro p{font-size:9.2px;line-height:11.6px;margin-top:12px}
.btn{display:inline-block;margin-top:16px;background:var(--bark);color:#fff;font-size:10px;width:102px;height:28px;line-height:28px;text-align:center;border-radius:2px}
.feature{position:absolute;top:551px;width:223px;height:176px;border:1px solid #999}
.feature-label{position:absolute;left:64px;top:-6px;width:102px;height:50px;background:var(--bark);color:#fff;font-size:18px;font-weight:300;text-align:center;line-height:48px;box-shadow:0 2px 3px rgba(0,0,0,.3)}
.training{left:333px;background:linear-gradient(180deg,#c8d2da 0%,#9fb0bd 60%,#5c7a3a 100%)}
.petcare{left:575px;background:linear-gradient(120deg,#d9e48a 0%,#e8d6c0 50%,#9ed2e0 100%)}
.tile{position:absolute;top:758px;width:162px;height:104px;border:1px solid #888}
.tile-label{position:absolute;left:0;bottom:0;background:rgba(123,65,36,.85);color:#fff;font-size:13px;font-weight:700;padding:3px 12px 4px}
.t-about{left:92px;background:linear-gradient(180deg,#7f9a5c,#b9a98c)}
.t-services{left:273px;background:linear-gradient(180deg,#4f86d6,#9cc7e8 70%,#4f9a2c)}
.t-photos{left:455px;background:linear-gradient(180deg,#6f8a4c,#c5b59a)}
.t-faq{left:636px;background:linear-gradient(120deg,#2c4f9a,#e9e0cc 60%,#2c4f9a)}
.quote-mark{position:absolute;left:92px;top:904px;font-size:58px;line-height:58px;font-weight:700;color:var(--bark-dark)}
.avatar{position:absolute;left:132px;top:896px;width:62px;height:62px;border:1px solid #bbb;background:linear-gradient(135deg,#a0522d,#e8c9a8)}
.testimonial{position:absolute;left:212px;top:898px}
.testimonial h3{font-size:15px;font-weight:400}
.testimonial .role{font-size:8px;color:var(--muted);margin-top:3px}
.testimonial p{font-size:11.5px;margin-top:13px}
.footer{position:absolute;left:92px;top:987px;width:706px;height:116px;background:var(--bark);color:#fff}
.footer-brand{position:absolute;left:26px;top:24px;width:66px;height:66px;border-radius:50%;background:#fff;border:3px solid var(--leaf);display:flex;align-items:center;justify-content:center;font-size:9px;font-weight:700;color:var(--bark)}
.assoc{position:absolute;left:102px;top:37px;font-size:9.5px;line-height:15.5px}
.tips{position:absolute;left:302px;top:22px;font-size:12px;line-height:15px}
.find{position:absolute;left:544px;top:22px;font-size:12px}
.circles{position:absolute;display:flex;gap:9px}
.circles span{width:27px;height:27px;border-radius:50%;background:#fff}
.copyright{position:absolute;top:1120px;left:0;width:890px;text-align:center;font-size:9.5px;color:#444}
</style>
</head>
<body>
<div class="backdrop" role="img" aria-label="Pale green paw-print pattern background"></div>
<div class="page"></div>
<div class="nav-tab-left"></div>
<div class="nav-tab-right"></div>
<div class="nav-band"></div>
<div class="brand"><span class="brand-name">PLUMCREST</span></div>

<div class="social-top"><span></span><span></span><span></span><span></span></div>
<div class="search">Search...
  <svg width="9" height="9" viewBox="0 0 10 10"><circle cx="4" cy="4" r="3" fill="none" stroke="#666" stroke-width="1.4"/><line x1="6.2" y1="6.2" x2="9" y2="9" stroke="#666" stroke-width="1.6"/></svg>
</div>
<nav class="main-nav">
  <span class="current">Home</span><span>About</span><span>Services / Rates</span><span>Photos / Videos</span><span>FAQ</span><span>Testimonials</span><span>PCW Tips</span><span>Store</span><span>Contact</span>
</nav>

<section class="hero" role="img" aria-label="Photo of a large dog hugged by a young child in an autumn park"></section>
<div class="hero-shadow"></div>
<div class="hero-copy">
  <h1 class="hero-title">Care for<br>your friend</h1>
  <p class="hero-sub">Call today to schedule an<br>appointment for your pet.</p>
  <span class="hero-btn">Learn More <svg width="11" height="11" viewBox="0 0 10 10"><path d="M1 0L10 5L1 10Z" fill="#fff"/></svg></span>
</div>
<div class="dots" style="left:430px;top:430px"><span></span><span></span><span class="on" style="background:#6b3a1f"></span></div>

<div class="welcome">Wel come...!!!</div>
<div class="intro">
  <h2>Learn to Train The Plumcrest Way: The Foundation + Training Workbook PDF</h2>
  <p>Internationally-renowned dog trainer, Owen Marsh, founder of 'Plumcrest Way Training and Rehabilitation' presents Learn to Train The Plumcrest Way: The Foundation. In this very special DVD series, Owen shares his unique approach to dog training in a clear, easy to follow, step-by-step fashion that takes the mystery and confusion out of creating a happy, healthy, and obedient dog.</p>
  <span class="btn">LEARN MORE</span>
</div>
<div class="feature training" role="img" aria-label="Photo of a shepherd dog leaping over a hurdle beside its trainer"><div class="feature-label">Training</div></div>
<div class="feature petcare" role="img" aria-label="Photo of a woman hugging a shaggy white dog"><div class="feature-label">Pet Care</div></div>

<div class="tile t-about" role="img" aria-label="Photo of a dog jumping through an agility hoop"><span class="tile-label">ABOUT US</span></div>
<div class="tile t-services" role="img" aria-label="Photo of a woman giving a command to a golden dog on grass"><span class="tile-label">SERVICES</span></div>
<div class="tile t-photos" role="img" aria-label="Photo of a dog walking on a leash beside its owner"><span class="tile-label">PHOTOS &amp; VEDIO</span></div>
<div class="tile t-faq" role="img" aria-label="Photo of two golden puppies"><span class="tile-label">FAQ</span></div>

<div class="quote-mark">“</div>
<div class="avatar" role="img" aria-label="Portrait of the trainer with her dog"></div>
<div class="testimonial">
  <h3>Lena Hart</h3>
  <div class="role">Trainer</div>
  <p>“What made Owen different from other trainers is that he actually listened to our problems and concerns”</p>
</div>
<div class="dots" style="left:433px;top:967px"><span class="on"></span><span></span><span></span></div>

<footer class="footer">
  <div class="footer-brand">PLUMCREST</div>
  <div class="assoc">Guild of Canine Educators<br>(GCE)<br>GCE#B-2315- Professional Level</div>
  <div class="tips">For more training tips,<br>insights, and information,</div>
  <div class="circles" style="left:302px;top:58px"><span></span><span></span><span></span><span></span><span></span></div>
  <div class="find">You can also find us at:</div>
  <div class="circles" style="left:544px;top:58px"><span></span><span></span></div>
</footer>
<div class="copyright">Plumcrest Way | COPYRIGHT © 2015 . ALL RIGHTS RESERVED</div>
</body>
</html>
```